Double sided customer happy holidays and thank you card

Create a simple holiday theme thank you and happy holidays card using white and red (CMYK 0.94.100.0) as the primary colors with a dash of green (CMYK 85.3.91.44) peppered in the color scheme.
1. draft for templates in portrait view using: 4x6, 5x7, 5.5x8.5, and 6x9 (templates guidelines with bleed, trim, and safe areas attached.
2. Make prominent use of the company logo and icons (attached).
3. Backside of the card is devoted to customer instructions (attached).
4. Frontside wording draft attached.
5. Signatures, Walter & Phoebe, should be in handwritten script.
6. Words should be in a super large font size so that print is easy to read for all customers.

```html
<!DOCTYPE html>
<html lang="en">
<head>
<meta charset="utf-8">
<title>Holiday Thank You Card</title>
<link rel="stylesheet" href="https://fonts.googleapis.com/css2?family=PT+Serif:ital,wght@1,400&display=swap">
<style>
  :root {
    --holiday-red: #ec0000;
    --card-white: #ffffff;
    --backdrop: #d9d9d9;
    --lettering-tone-a: #f3f0f0;
    --lettering-tone-b: #ffffff;
  }
  * { margin: 0; padding: 0; box-sizing: border-box; }
  html, body {
    width: 1200px;
    height: 1200px;
    overflow: hidden;
    background: var(--backdrop);
  }
  .card {
    position: absolute;
    left: 200px;
    top: 0;
    width: 800px;
    height: 1200px;
    background: var(--card-white);
    overflow: hidden;
    font-family: "PT Serif", Georgia, serif;
    font-style: italic;
    color: var(--card-white);
  }
  .card__scallop-band {
    position: absolute;
    inset: 0;
    width: 800px;
    height: 1200px;
  }
  .card__scallop-band path { fill: var(--holiday-red); }
  .card__headline-lettering {
    position: absolute;
    left: 248px;
    top: 40px;
    width: 311px;
    height: 261px;
    border-radius: 40px;
    background: radial-gradient(ellipse at center, rgba(255,255,255,0.22), rgba(255,255,255,0.04) 70%, rgba(255,255,255,0));
  }
  .card__message {
    position: absolute;
    left: 90px;
    top: 346px;
    width: 620px;
    text-align: center;
    font-size: 37px;
    line-height: 47px;
  }
  .card__signoff {
    position: absolute;
    left: 100px;
    top: 866px;
    width: 600px;
    text-align: center;
    font-size: 42px;
    line-height: 52px;
  }
  .card__brand {
    position: absolute;
    left: 0;
    top: 1008px;
    width: 800px;
    text-align: center;
  }
  .card__brand-mark {
    display: block;
    width: 62px;
    height: 62px;
    margin: 0 auto 8px;
    border: 2px solid var(--card-white);
    border-radius: 50%;
  }
  .card__brand-name {
    font-size: 52px;
    line-height: 60px;
  }
</style>
</head>
<body>
  <main class="card">
    <svg class="card__scallop-band" viewBox="0 0 800 1200" aria-hidden="true">
      <path d="M25,-68 C25,-3 88,-3 88,61 C88,126 25,126 25,190 C25,255 88,255 88,319 C88,384 25,384 25,448 C25,513 88,513 88,577 C88,642 25,642 25,706 C25,771 88,771 88,835 C88,900 25,900 25,964 C25,1029 88,1029 88,1093 C88,1158 25,1158 25,1222 L775,1222 C775,1158 712,1158 712,1093 C712,1029 775,1029 775,964 C775,900 712,900 712,835 C712,771 775,771 775,706 C775,642 712,642 712,577 C712,513 775,513 775,448 C775,384 712,384 712,319 C712,255 775,255 775,190 C775,126 712,126 712,61 C712,-3 775,-3 775,-68 Z"/>
    </svg>

    <div class="card__headline-lettering" role="img" aria-label="Hand-lettered white script reading Thank you"></div>

    <p class="card__message">
      We are thankful for the opportunity to be a VIP at your table this holiday season although not for long, we're sure!<br>
      Thanks for allowing us to be a part of your moments this year and this holiday season. We are in your debt. May we be the first to wish you Happy Holidays and Happy New Year!
    </p>

    <p class="card__signoff">
      Cheers by the pound!<br>
      Walter &amp; Phoebe
    </p>

    <div class="card__brand">
      <span class="card__brand-mark"></span>
      <span class="card__brand-name">Ringloaf</span>
    </div>
  </main>
</body>
</html>
```